Music Industry Business Needs a Business Card Design

Copper Lantern is an audio mastering company that has been in business for 20 years. Mastering is the final creative step in the music production chain. Our job is to make the music sound as good as it possibly can prior to release to the public. Our world is technical, artistic, precise. We work on everything from independent artists to the music for the Grandfield Cup. We are looking for a new, more modern business card design. I am uploading a copy of our logo, although it doesn't absolutely need to be included in the design.

Target Market(s)

Music Industry Professionals

Industry/Entity Type

Business

Contact Information for Business Card

Address, Phone, Email, Website, Name, Job Title

Font styles to use
Sans Serif

Requirements
Must have
• Sorry, but I don't have any concrete things to request. If I had a clear idea of what I want, I would probably just design something myself. I am looking for fresh input and thought I would try this.
Should not have
• Anything that is typical, such as headphones or the like.

```html
<!DOCTYPE html>
<html lang="en">
<head>
<meta charset="utf-8">
<title>Copper Lantern – Business Card</title>
<link rel="stylesheet" href="https://fonts.googleapis.com/css2?family=Open+Sans:wght@400;600;700&display=swap">
<style>
  :root {
    --page: #ffffff;
    --card: #ffffff;
    --shadow: #a9a9a9;
    --ink: #1a1a1a;
    --accent: #9b1b1b;
    --red: #e53a2f;
    --orange: #f39a1d;
    --yellow: #f3e14a;
    --green: #5fb946;
    --cyan: #36b6d8;
    --blue: #2b55b8;
    --purple: #8a3f9c;
    --pink: #e0417f;
    --spectrum: linear-gradient(90deg, var(--red), var(--orange) 14%, var(--yellow) 28%, var(--green) 45%, var(--cyan) 62%, var(--blue) 78%, var(--purple) 90%, var(--pink));
  }
  * { margin: 0; padding: 0; box-sizing: border-box; }
  html, body {
    width: 1200px; height: 402px; overflow: hidden;
    background: var(--page);
    font-family: "Open Sans", Arial, sans-serif;
    color: var(--ink);
  }
  .canvas { position: relative; width: 1200px; height: 402px; }

  .card {
    position: absolute;
    background: var(--card);
    box-shadow: 6px 6px 0 var(--shadow);
    overflow: hidden;
  }
  .card--front { left: 12px; top: 14px; width: 576px; height: 368px; }
  .card--back  { left: 606px; top: 14px; width: 572px; height: 366px; }

  .brand-name {
    position: absolute;
    font-weight: 400;
    color: var(--ink);
    white-space: nowrap;
    letter-spacing: 0.5px;
  }
  .card--front .brand-name { left: 36px; top: 100px; font-size: 24px; }
  .card--back .brand-name { left: 0; right: 0; top: 122px; text-align: center; font-size: 42px; }

  .equalizer-art {
    position: absolute; left: 14px; top: 158px; width: 250px; height: 210px;
    background: linear-gradient(90deg, var(--orange), var(--pink) 25%, var(--green) 50%, var(--cyan) 72%, var(--purple) 88%, var(--pink));
    -webkit-mask-image: linear-gradient(180deg, transparent 0%, rgba(0,0,0,.5) 35%, #000 75%);
    mask-image: linear-gradient(180deg, transparent 0%, rgba(0,0,0,.5) 35%, #000 75%);
  }

  .contact { position: absolute; left: 292px; top: 52px; }
  .contact__name { font-size: 20px; font-weight: 700; color: var(--accent); line-height: 28px; }
  .contact__role { font-size: 18px; font-weight: 700; margin-top: 6px; line-height: 24px; }
  .contact__address { font-size: 16px; line-height: 30px; margin-top: 10px; }

  .contact-list { position: absolute; left: 291px; top: 236px; list-style: none; }
  .contact-list li {
    display: flex; align-items: center; height: 29.5px;
    font-size: 16px;
  }
  .contact-list svg { width: 25px; height: 25px; margin-right: 20px; flex: none; }

  .spectrum-art {
    position: absolute; left: 0; top: 150px; width: 572px; height: 180px;
    background: var(--spectrum);
    -webkit-mask-image: linear-gradient(180deg, transparent 0%, rgba(0,0,0,.55) 45%, #000 100%);
    mask-image: linear-gradient(180deg, transparent 0%, rgba(0,0,0,.55) 45%, #000 100%);
  }
  .spectrum-reflection {
    position: absolute; left: 0; top: 330px; width: 572px; height: 36px;
    background: var(--spectrum);
    opacity: .45;
    -webkit-mask-image: linear-gradient(180deg, #000, transparent);
    mask-image: linear-gradient(180deg, #000, transparent);
  }
</style>
</head>
<body>
<main class="canvas">

  <section class="card card--front">
    <div class="brand-name">COPPER LANTERN</div>

    <div class="equalizer-art" role="img" aria-label="Colourful equalizer bar graphic"></div>

    <div class="contact">
      <div class="contact__name">Name</div>
      <div class="contact__role">Position</div>
      <div class="contact__address">
        118 - 7th Avenue S.W.<br>
        Riverton, Alberta, Canada<br>
        T5K 2P8
      </div>
    </div>

    <ul class="contact-list">
      <li>
        <svg viewBox="0 0 24 24" aria-hidden="true">
          <circle cx="12" cy="12" r="10.5" fill="none" stroke="#9b1b1b" stroke-width="1.8"/>
          <path d="M8.2 6.8c.6-.5 1.3-.3 1.6.3l1 1.9c.2.5.1 1-.3 1.3l-.8.6c.6 1.4 1.6 2.5 3 3.2l.7-.8c.4-.4.9-.5 1.3-.2l1.9 1.1c.6.3.7 1 .3 1.6-.9 1.1-2.2 1.5-3.5.9-2.9-1.3-4.9-3.4-6-6.3-.4-1.3 0-2.7.8-3.6z" fill="#9b1b1b"/>
        </svg>
        (403) 555 - 0187
      </li>
      <li>
        <svg viewBox="0 0 24 24" aria-hidden="true">
          <rect x="2" y="6" width="20" height="13" fill="#9b1b1b"/>
          <path d="M2 6l10 7 10-7" fill="none" stroke="#fff" stroke-width="1.4"/>
        </svg>
        info@copperlantern.ca
      </li>
      <li>
        <svg viewBox="0 0 24 24" aria-hidden="true">
          <circle cx="12" cy="12" r="10" fill="#9b1b1b"/>
          <g fill="none" stroke="#fff" stroke-width="1.2">
            <ellipse cx="12" cy="12" rx="4.2" ry="10"/>
            <line x1="12" y1="2" x2="12" y2="22"/>
            <line x1="2" y1="12" x2="22" y2="12"/>
            <path d="M4 7h16M4 17h16"/>
          </g>
        </svg>
        www.copperlantern.ca
      </li>
    </ul>
  </section>

  <section class="card card--back">
    <div class="spectrum-art" role="img" aria-label="Rainbow audio spectrum bar graphic"></div>
    <div class="spectrum-reflection" aria-hidden="true"></div>
    <div class="brand-name">COPPER LANTERN</div>
  </section>

</main>
</body>
</html>
```